Hair Restoration Center needs a new classy clean professional look for a new website.

We want a new look for our outdated website. We are a high end hair restoration company who deals with all kinds of hair loss for both men and women. We offer solutions to hair loss prevention or our state of the art non surgical hair restoration. Our look would be similar to the medical enhancement designs. We are doctor endorsed and very professional. We are looking for a clean look, positive vibe, strong imagery.
People with hair loss are often in distress, feeling a lack of self esteem, and looking for a reliable solution. the difference between our clients is some come to us for hair loss prevention or for hair restoration depends on how advanced their loss has become or the kind of loss. Younger people tend to be prevention candidates, often having treatments done at home, whereas medical loss for women or mens advanced hair loss become restoration clients. Prevention age ranges from early 20's to 40's and restoration can be any age if medical or for women and men usually late 30's onward.
Our site is dated and doesnt represent us well but if you want to read more about us you can visit www.velmarhair.com. the photos attached here are also blown up in large posters throughout the office and models of non surgical restoration. For a large selection of photos please go to the link. There is one before photo but many types of after photos for each model.
There are more colours of the logos available in grey and dark greyish green available. http://www.velmarhair.com/download/Models_Before_After.zip
Our primary means of new business comes from internet searches.
Your task is to design the home page design but the site will need to link into a women's section and a mens section along with gender neutral educational pages. You will get a feel from our current site. Www.velmarhair.com
Content will be rewritten but I gave a couple samples to use as fill in. Our current site has way to much content and I would like to step away from all of it. you can utilize fill in text of any kind as a sample
To get a feel of our office, it is black granite, white rock features with floor to ceiling beautiful city and ocean views. very high end.

Target Market(s)

men and women of all ages as listed above

Industry/Entity Type

Internet

Number of Pages Required

1 page

Requirements
Must have
• imagery and design that creates emotion - consider that people with hair loss is emotional buyers and the sites image needs to speak to that.
• it would create a sense of security and confidence in choosing us to help them in a time of need.
• also a sense of ease flowing through the site where women can go to a dedicated area and men have their own area of the site. each area needs to cater to the two divisions prevention and restoration and also speak and visually appeal to the different sexes. You can get a feel of this by visiting www.velmarhair.com
Nice to have
• I have video footage from a green room that could be worked on to add in
• wordpress preferred
Should not have
• no humour
• do not focus on the before photos as primary focus but the afters with the ability to see the before.

```html
<!DOCTYPE html>
<html lang="en">
<head>
<meta charset="utf-8">
<title>Velmar Hair Restoration Centre</title>
<link href="https://fonts.googleapis.com/css2?family=Oswald:wght@400;500&family=Lato:ital,wght@0,400;0,700;1,400;1,700&display=swap" rel="stylesheet">
<style>
:root{
  --red:#c8141e;
  --slate:#4d5a5c;
  --slate-dark:#3a4547;
  --teal-grey:#6e8184;
  --ink:#3b3b3b;
  --band:#333333;
  --band-dark:#2a2a2a;
  --footer:#2e2e2e;
  --footer-bottom:#1f1f1f;
  --text-grey:#666;
  --light:#f2f2f2;
  --white:#fff;
}
*{box-sizing:border-box;margin:0;padding:0}
html,body{width:1200px;height:2390px;overflow:hidden;background:var(--white)}
body{position:relative;font-family:"Lato",sans-serif;color:var(--ink)}
.abs{position:absolute}
.oswald{font-family:"Oswald",sans-serif}

/* header */
.site-header{left:0;top:0;width:1200px;height:160px;background:linear-gradient(#fff,#e9ecec)}
.brand{left:142px;top:18px}
.brand-name{font-family:"Oswald",sans-serif;font-size:74px;font-weight:400;color:var(--slate);line-height:1;letter-spacing:1px}
.brand-tag{font-family:"Oswald",sans-serif;font-size:18px;color:var(--slate);margin-left:170px;margin-top:2px}
.book{left:654px;top:40px;width:204px;height:60px;background:linear-gradient(#fff,#dcdcdc);border:1px solid #ddd;text-align:center;font-family:"Oswald",sans-serif}
.book .small{color:var(--red);font-size:17px;margin-top:4px}
.book .big{color:var(--slate);font-size:25px;line-height:1.1}
.partner-badge{left:930px;top:18px;width:126px;height:40px;background:var(--slate);border-top:6px solid var(--red)}
.phone{left:888px;top:70px;font-family:"Oswald",sans-serif;font-style:normal;font-size:26px;color:var(--slate);display:flex;align-items:center;gap:8px}
.phone svg{width:26px;height:26px}

.main-nav{left:142px;top:135px;width:916px;height:52px;background:linear-gradient(#5b686a,#3f4a4c);display:flex;align-items:center;justify-content:space-between;padding:0 12px;box-shadow:0 3px 6px rgba(0,0,0,.3);z-index:3}
.main-nav a{font-family:"Oswald",sans-serif;color:#fff;text-decoration:none;font-size:19px;padding:0 10px;position:relative}
.main-nav a.active{color:var(--red)}
.main-nav a.active::after{content:"";position:absolute;left:50%;bottom:-14px;margin-left:-7px;border:7px solid transparent;border-bottom-color:var(--red)}

/* hero */
.hero{left:0;top:160px;width:1200px;height:537px;background:linear-gradient(110deg,#f4f4f4 0%,#dcdfe0 45%,#c9cdce 100%)}
.hero-photo{left:470px;top:0;width:560px;height:537px;background:radial-gradient(ellipse at 50% 55%,#6d5a4e 0%,#55504c 45%,#a8abac 80%,transparent 100%)}
.hero-caption{left:142px;top:318px;width:512px;height:115px;background:rgba(80,80,80,.75)}
.hero-line{font-family:"Oswald",sans-serif;color:#fff;font-style:italic;position:absolute;white-space:nowrap}
.hero-line .hl{background:var(--red);padding:0 8px;font-size:48px;font-style:normal}
.l1{left:20px;top:4px;font-size:30px}
.l2{left:90px;top:58px;font-size:30px}
.dots{display:flex;gap:6px}
.dots span{width:8px;height:8px;border-radius:50%;background:#ccc}
.dots span:first-child{background:var(--red)}
.hero .dots{position:absolute;right:144px;bottom:28px}

/* welcome */
.welcome{left:0;top:697px;width:1200px;height:203px;background:linear-gradient(var(--band),var(--band-dark));text-align:center;color:#fff}
.welcome h1{font-family:"Oswald",sans-serif;font-weight:400;font-size:40px;margin-top:20px;color:#ddd}
.welcome h1 span,.gallery h2 span{color:var(--teal-grey)}
.welcome p{width:900px;margin:14px auto 0;font-style:italic;font-size:14.5px;line-height:24px;color:#ddd}
.welcome p a{color:var(--red)}
.notch{width:0;height:0;border:18px solid transparent;border-top-color:var(--band-dark);left:582px}

/* tabs */
.tabs{left:142px;top:950px;width:916px;height:42px;border-bottom:5px solid #d5d5d5;display:flex;justify-content:space-between;padding:0 30px}
.tabs a{font-family:"Oswald",sans-serif;color:var(--slate);text-decoration:none;font-size:21px;padding-bottom:6px;position:relative}
.tabs a.active::after{content:"";position:absolute;left:-6px;right:-6px;bottom:-5px;height:5px;background:var(--red)}
.panel{left:142px;top:1020px;width:914px;height:280px;background:linear-gradient(#fff,#eef0f1);border:1px solid #e4e4e4;box-shadow:0 18px 18px -14px rgba(0,0,0,.35)}
.panel h3{position:absolute;left:28px;top:26px;font-style:italic;font-weight:400;font-size:23px;color:var(--slate)}
.panel p{position:absolute;left:26px;top:68px;width:490px;font-style:italic;font-size:14px;line-height:24px;color:var(--text-grey)}
.panel-photo{right:0;top:0;width:450px;height:278px;background:linear-gradient(120deg,#fff 0 22%,#7e7e7e 22% 24%,#bdbdbd 24%,#8d8a86 60%,#5a6d86 100%);clip-path:polygon(28% 0,100% 0,100% 100%,0 100%)}
.go{left:0;bottom:0;width:28px;height:28px;background:var(--red);display:flex;align-items:center;justify-content:center}

/* gallery */
.gallery{left:0;top:1363px;width:1200px;height:306px;background:linear-gradient(var(--band),var(--band-dark));text-align:center}
.gallery h2{font-family:"Oswald",sans-serif;font-weight:400;font-size:38px;color:#ddd;margin-top:5px}
.card{top:62px;width:261px;height:196px;border:5px solid #555;display:flex}
.card div{flex:1;position:relative}
.card span{position:absolute;bottom:4px;right:8px;font-family:"Oswald",sans-serif;color:#fff;font-size:19px}
.arrow{top:140px;width:0;height:0;border:14px solid transparent}
.arrow.prev{left:110px;border-right-color:#888}
.arrow.next{left:1058px;border-left-color:#888}

/* testimonials */
.testi-title{left:0;top:1700px;width:1200px;text-align:center;font-family:"Oswald",sans-serif;font-size:34px;color:var(--slate)}
.testi{left:142px;top:1782px;width:916px;height:204px;background:linear-gradient(#fff,#eceeef);border:1px solid #e6e6e6;box-shadow:0 18px 18px -14px rgba(0,0,0,.35)}
.testi-photo{left:0;top:0;width:200px;height:204px;background:linear-gradient(135deg,#d8d8d8,#5a4a42);clip-path:polygon(0 0,100% 0,60% 100%,0 100%)}
.testi blockquote{position:absolute;left:225px;top:32px;width:660px;font-style:italic;font-size:14px;line-height:24px;color:var(--text-grey);text-indent:46px}
.quote-mark{position:absolute;left:222px;top:20px;font-family:"Oswald",sans-serif;font-size:60px;color:#ccc;line-height:1}
.testi cite{position:absolute;left:225px;top:140px;font-style:normal;font-weight:700;color:var(--red);font-size:15px}
.testi small{position:absolute;left:230px;top:162px;font-size:12px;color:#888}
.testi .dots{position:absolute;right:12px;bottom:12px}

/* footer */
.site-footer{left:0;top:2066px;width:1200px;height:290px;background:var(--footer);color:#ddd}
.site-footer h4{font-family:"Oswald",sans-serif;font-weight:400;font-size:20px;color:#fff;position:absolute;top:14px}
.links{left:145px;top:60px;list-style:none;font-size:12.5px;line-height:26.5px}
.links li::before{content:"› ";color:#aaa}
.links li.active{color:var(--red)}
.city-tabs{left:302px;top:60px;width:470px;border-bottom:1px solid #555;display:flex;gap:40px;font-size:12.5px;padding-bottom:8px}
.city-tabs .active{color:var(--red)}
.contact{left:302px;top:100px;font-size:12.5px;line-height:20px}
.contact .row{display:flex;align-items:center;gap:8px;margin-top:12px}
.contact svg{width:14px;height:14px;fill:#ddd}
.map{left:525px;top:127px;width:252px;height:146px;border:8px solid #444;background:linear-gradient(135deg,#e8e6df,#cfcac0)}
.video{left:810px;top:61px;width:250px;height:153px;background:linear-gradient(135deg,#d7d3d0,#7a5238)}
.video-bar{left:810px;top:214px;width:250px;height:14px;background:#bbb}
.video-brand{left:850px;top:232px;font-family:"Oswald",sans-serif;font-size:36px;color:#555}
.bottom-bar{left:0;top:2356px;width:1200px;height:34px;background:var(--footer-bottom);color:#ddd;font-size:12.5px;padding:9px 142px}
.social{right:140px;top:6px;display:flex;gap:6px}
.social span{width:22px;height:22px;border-radius:50%;background:#3b5b9a}
.social span:nth-child(2){background:#2aa9e0}
.social span:nth-child(3){background:#555}
</style>
</head>
<body>

<header class="site-header abs">
  <div class="brand abs">
    <div class="brand-name">Velmar</div>
    <div class="brand-tag">Hair Restoration Centre</div>
  </div>
  <div class="book abs"><div class="small">Free Consultation</div><div class="big">BOOK NOW</div></div>
  <div class="partner-badge abs" role="img" aria-label="Partner badge"></div>
  <div class="phone abs">
    <svg viewBox="0 0 26 26"><rect width="26" height="26" rx="5" fill="#4d5a5c"/><path d="M8 6l3 0 1 4-2 1c1 2 3 4 5 5l1-2 4 1 0 3c0 1-1 2-2 2C12 20 6 14 6 8c0-1 1-2 2-2z" fill="#fff"/></svg>
    <span>(555) 014 2270</span>
  </div>
</header>

<nav class="main-nav abs">
  <a class="active" href="#">Home</a><a href="#">Men</a><a href="#">Women</a><a href="#">Crown Advantage</a><a href="#">Blog Site</a><a href="#">Hairloss Facts</a><a href="#">Testimonies</a><a href="#">Contact Us</a>
</nav>

<section class="hero abs">
  <div class="hero-photo abs" role="img" aria-label="Woman with full wavy hair and man in grey blazer"></div>
  <div class="hero-caption abs">
    <div class="hero-line l1">Its not just <span class="hl">hair replacement,</span></div>
    <div class="hero-line l2">its <span class="hl">confidence</span> replacement!</div>
  </div>
  <div class="dots"><span></span><span></span><span></span><span></span></div>
</section>

<section class="welcome abs">
  <h1>Welcome to <span>Velmar</span></h1>
  <p>Sed ut perspiciatis unde omnis iste natus error sit voluptatem accusantium doloremque laudantium, totam rem aperiam, eaque ipsa quae ab illo inventore veritatis et quasi architecto beatae vitae dicta sunt explicabo. Nemo enim ipsam voluptatem quia voluptas sit aspernatur aut odit aut voluptas sit aspernatur aut odit aut fugit. <a href="#">More</a></p>
</section>
<div class="notch abs" style="top:900px"></div>

<nav class="tabs abs">
  <a class="active" href="#">Men Hair Solutions</a><a href="#">Women&nbsp; Hair Solutions</a><a href="#">Crown Advantage</a><a href="#">Hair Loss Facts</a>
</nav>
<article class="panel abs">
  <h3>Nemo enim ipsam voluptatem quia voluptas</h3>
  <p>Sed ut perspiciatis unde omnis iste natus error sit voluptatem accusantium doloremque laudantium, totam rem aperiam, eaque ipsa quae ab illo inventore veritatis et quasi architecto beatae vitae dicta sunt explicabo. Nemo enim ipsam voluptatem quia voluptas sit aspernatur aut odit aut voluptas sit aspernatur aut odit aut fugit. Nemo enim ipsam voluptatem quia voluptas sit aspernatur aut odit aut voluptas sit aspernatur aut odit aut fugit.</p>
  <div class="panel-photo abs" role="img" aria-label="Man with short styled hair in profile"></div>
  <a class="go abs" href="#"><svg width="16" height="16" viewBox="0 0 16 16"><path d="M2 8h10M8 3l5 5-5 5" stroke="#fff" stroke-width="2.4" fill="none"/></svg></a>
</article>

<section class="gallery abs">
  <h2>Before After <span>Gallery</span></h2>
  <div class="arrow prev abs"></div>
  <div class="card abs" style="left:171px"><div style="background:linear-gradient(#7b6a78,#3448a8)" role="img" aria-label="Balding man before treatment"><span>Before</span></div><div style="background:linear-gradient(#6a6a6a,#3a3a3a)" role="img" aria-label="Same man after restoration"><span>After</span></div></div>
  <div class="card abs" style="left:472px"><div style="background:linear-gradient(#e6e6e6,#b9a99c)" role="img" aria-label="Woman with hair loss before treatment"><span>Before</span></div><div style="background:linear-gradient(#eee,#7a4a34)" role="img" aria-label="Same woman after restoration"><span>After</span></div></div>
  <div class="card abs" style="left:775px"><div style="background:linear-gradient(#dcdcdc,#8d8d8d)" role="img" aria-label="Man with thinning hair before treatment"><span>Before</span></div><div style="background:linear-gradient(#d9d9d9,#6e7f96)" role="img" aria-label="Same man after restoration"><span>After</span></div></div>
  <div class="arrow next abs"></div>
</section>
<div class="notch abs" style="top:1669px"></div>

<h2 class="testi-title abs">Some Testimonials from Customers</h2>
<article class="testi abs">
  <div class="testi-photo abs" role="img" aria-label="Smiling client with dark hair"></div>
  <div class="quote-mark">&ldquo;</div>
  <blockquote>Sed ut perspiciatis unde omnis iste natus error sit voluptatem accusantium doloremque laudantium, totam rem aperiam, eaque ipsa quae ab illo inventore veritatis et quasi architecto beatae vitae dicta sunt explicabo. Nemo enim ipsam voluptatem quia voluptas sit aspernatur aut odit aut voluptas sit aspernatur aut odit aut fugit.</blockquote>
  <cite>-Maren</cite>
  <small>Emo enim</small>
  <div class="dots"><span></span><span></span><span></span><span></span></div>
</article>

<footer class="site-footer abs">
  <h4 style="left:145px">Quick Links</h4>
  <h4 style="left:302px">Quick Contact</h4>
  <h4 style="left:816px">Latest Video</h4>
  <ul class="links abs">
    <li class="active">Home</li><li>Men</li><li>Women</li><li>Natural</li><li>Blog Site</li><li>Hairloss Facts</li><li>Testimonies</li><li>Contact Us</li>
  </ul>
  <div class="city-tabs abs"><span class="active">VANCOUVER BC</span><span>VICTORIA BC</span><span>CALGARY AC</span></div>
  <address class="contact abs" style="font-style:normal">
    Suite 204, 88 Harbour Lane, V6A 1K2<br>Harbour Point, North Tower
    <div class="row"><svg viewBox="0 0 14 14"><path d="M3 1h3l1 3-2 1c1 2 2 3 4 4l1-2 3 1v3c0 1-1 2-2 2C6 13 1 8 1 3c0-1 1-2 2-2z"/></svg>+604 - 555 - 0147</div>
    <div class="row"><svg viewBox="0 0 14 14"><rect x="3" y="1" width="8" height="4"/><rect x="1" y="5" width="12" height="6"/><rect x="3" y="9" width="8" height="4" fill="#2e2e2e" stroke="#ddd"/></svg>+604 - 555 - 0148</div>
    <div class="row"><svg viewBox="0 0 14 14"><rect x="1" y="3" width="12" height="8"/><path d="M1 3l6 5 6-5" stroke="#2e2e2e" fill="none"/></svg>info@velmarhair.com</div>
  </address>
  <div class="map abs" role="img" aria-label="Street map of office location"></div>
  <div class="video abs" role="img" aria-label="Video still of woman with curly hair"></div>
  <div class="video-bar abs"></div>
  <div class="video-brand abs">Velmar</div>
</footer>
<div class="bottom-bar abs">
  © Copyright 2015 Velmar . All Rights Reserved
  <div class="social abs"><span></span><span></span><span></span></div>
</div>

</body>
</html>
```